Doctor to Patient Management Website

I need a design for a health management website that connects doctors to patients. The website will consist of: A main page mainly describing our goal, services, and initiatives towards (Who we are AKA "About Us", Our services, Contact Us, Quick Links for health tips, Language selection, Find a doctor, search bar, Member Login Section, small glossary section below with links to all entities mentioned prior, Help section (Helpful tips and tutorials, Used to request help from admin, customer service, to resolve issues or get assistance). A profile page with two types:1) Doctor Profile: Doctor Personal info (First, Last, Middle Name, Title), Clinic, Hospital Info, Department, Credentials, Years of Experience, Patients rating, #Patients seen during the current week, #Patients seen in total, Picture, Link to email doctor, Link to print doctor's profile). Tabs for "About Me", "Contact Info", "Ratings & Comments", "Documents" (To be downloaded and uploaded by patient), "Patients (List of Patients alphabetical order by name)", "Calendar" (to see doctor's availability for booking) underneath all links. 2) Patient profile: About me, Personal Info, Height, Weight, Blood Type, Age, DOB, Name, etc..., Message and email link.Picture of patient with menu made of "Personal Data", "Biometrics", "Allergies", "Illnesses", "Medications", "Medical Procedures", "Doctors" treating the patient, "Documents" (To be downloaded and uploaded by patient). Underneath all, other patients he or she is related to (For example: family member, so patient can't connect to other patients who are family members)3) Login section: New Users will have option to register using:First Name (Required), Last Name, Middle (not required), Address (Not required), City (Required), Country (Required), Email (Not required), Phone Number (Required), Choose UserName, Password, Account Type (Doctor or Patient). Once registered, they will log in using UserName, Password, and Account_Type.Curent Users will log in using UserName, Password, and Account_Type and option to retrieve username or password.Pages to include (Login Page - Registration Page - Retrieve Username and Reset Password Page)Please see link below:https://lanternpost-media.example/importance-claiming-vitalrank-quopa-zeltra/Pictures are attached to this project as an inspirationFYI: Dummy text can be used to fill in the business, services, and descriptive information. Feel free to include your own ideas in the layout, design, categories, patterns, and more to and showcase your talent. Design and pictures provided are available as source of ideas.

Target Market(s)

Age: 21+ / Family Oriented / Medical Sector / Metropolitan Area / Educated and non Educated Users

Industry/Entity Type

Health Care

Number of Pages Required

5+ page

Font styles to use
Sans Serif

Colors

Designer to choose colors to be used in the design.

Requirements
Must have
• Thin layer design
• Simple font - No serif
• Clean menu with light but solid colors (No Gradient effect)
Nice to have
• Different color themes (2 or 3) can be combined
• Sample pictures for illustration (either as an ad or to go with the flow of your design)
• Dashboard Feel (Suggested but not required)
Should not have
• Artistic fonts - with Serif
• Dark color themes

```html
<!DOCTYPE html>
<html lang="en">
<head>
<meta charset="utf-8">
<title>Medvira – Find a Doctor</title>
<link href="https://fonts.googleapis.com/css2?family=Lato:wght@300;400;700;900&display=swap" rel="stylesheet">
<style>
:root{
  --blue:#1f7fc0;
  --blue-dark:#17679f;
  --ink:#222;
  --muted:#777;
  --grey-bg:#f1f1f1;
  --footer:#1f2a33;
  --footer-text:#dfe4e8;
  --white:#fff;
}
*{margin:0;padding:0;box-sizing:border-box}
html,body{width:1200px;height:4852px;overflow:hidden}
body{font-family:'Lato',sans-serif;color:var(--ink);position:relative;background:var(--white)}
.abs{position:absolute}
.center{left:0;width:1200px;text-align:center}
a{color:inherit;text-decoration:none}

/* hero */
.hero{top:0;left:0;width:1200px;height:780px;overflow:hidden}
.hero-photo{position:absolute;inset:0;background:linear-gradient(120deg,#4d5a66 0%,#7d8994 40%,#a9b1b8 65%,#56626d 100%)}
.hero-shade{position:absolute;inset:0;background:rgba(20,28,36,.45)}
.logo{left:113px;top:58px;font-size:38px;font-weight:700;color:var(--white)}
.nav{top:70px;left:375px;display:flex;gap:22px;font-size:13px;color:var(--white);align-items:center}
.member-btn{left:830px;top:60px;width:164px;height:42px;border-radius:21px;background:var(--blue);color:var(--white);font-size:13px;font-weight:700;display:flex;align-items:center;justify-content:center;gap:8px}
.lang{left:1010px;top:64px;width:76px;height:34px;border:1px solid rgba(255,255,255,.6);color:var(--white);font-size:12px;display:flex;align-items:center;justify-content:center;gap:5px}
.lang i{width:14px;height:9px;background:#c9c9c9;display:inline-block}
.hero-title{top:290px;font-size:74px;font-weight:900;color:var(--white);letter-spacing:1px}
.hero-lead{top:405px;font-size:17px;line-height:30px;color:var(--white)}
.search{left:298px;top:505px;width:602px;height:52px;border-radius:26px;background:var(--white);border:2px solid var(--blue)}
.search span{position:absolute;left:36px;top:15px;font-size:14px;color:#777}
.search-btn{position:absolute;right:-2px;top:-2px;width:118px;height:52px;border-radius:0 26px 26px 0;background:var(--blue);color:var(--white);font-size:14px;font-weight:700;display:flex;align-items:center;justify-content:center;gap:7px}
.dots{top:706px;left:550px;display:flex;gap:10px}
.dots i{width:12px;height:12px;border-radius:50%;background:var(--white);display:block}
.dots i.on{background:var(--blue)}

/* section headings */
.ghost{font-size:80px;font-weight:900;color:rgba(0,0,0,.05);letter-spacing:2px;white-space:nowrap}
.ghost.light{color:rgba(255,255,255,.08)}
.sec-title{font-size:44px;font-weight:700}
.sec-sub{font-size:15px;color:var(--muted)}
.rule{width:62px;height:3px;background:var(--blue);left:569px}

/* services */
.service{width:300px;text-align:center}
.service h3{font-size:16px;font-weight:700;margin-top:18px}
.service p{font-size:13px;line-height:25px;color:var(--muted);margin-top:14px}
.pill{height:58px;border-radius:29px;background:var(--blue);color:var(--white);font-size:14px;font-weight:700;display:flex;align-items:center;justify-content:center;gap:8px}

/* about */
.about{top:1731px;left:0;width:1200px;height:637px;background:var(--grey-bg)}
.about-title{left:113px;top:1853px;font-size:44px;font-weight:700}
.about-ghost{left:330px;top:1840px}
.about-text{left:113px;top:1975px;width:420px;font-size:13.5px;line-height:28px;color:var(--muted)}
.read-btn{left:113px;top:2186px;width:155px;height:48px;border-radius:24px;background:var(--blue);color:var(--white);font-size:14px;font-weight:700;display:flex;align-items:center;justify-content:center;gap:7px}
.photo{box-shadow:0 3px 12px rgba(0,0,0,.18)}
.about-photo{left:556px;top:1850px;width:531px;height:405px;background:linear-gradient(110deg,#c9d5de,#e8edf1 45%,#9fb3c4);border:6px solid var(--white)}

/* tips */
.tips{top:2368px;left:0;width:1200px;height:848px;background:var(--blue)}
.tips-photo{left:129px;top:2708px;width:534px;height:359px;background:linear-gradient(120deg,#6f8aa0,#d6dde2 50%,#8da4b6)}
.tips-box{left:634px;top:2685px;width:453px;height:398px;border:2px solid rgba(255,255,255,.8)}
.tips-list{left:718px;top:2735px;list-style:none;color:var(--white);font-size:14px}
.tips-list li{height:33.5px;display:flex;align-items:center;gap:20px}
.outline-btn{left:718px;top:2980px;width:155px;height:46px;border:2px solid var(--white);border-radius:23px;color:var(--white);font-size:14px;font-weight:700;display:flex;align-items:center;justify-content:center;gap:7px}

/* help */
.video{left:236px;top:3571px;width:728px;height:408px;background:linear-gradient(110deg,#a9bccb,#e3e8ec 45%,#7f9bb1);border:6px solid var(--white)}
.help-list{top:4045px;list-style:none;font-size:17px;color:var(--ink)}
.help-list li{height:46px;display:flex;align-items:center;gap:14px}

/* footer */
.footer{top:4425px;left:0;width:1200px;height:427px;background:var(--footer)}
.footer-text{color:var(--footer-text)}
.f-head{top:4500px;font-size:15px;font-weight:700;color:var(--white)}
.f-list{list-style:none;font-size:12.5px}
.f-list li{height:33px;display:flex;align-items:center;gap:18px}
.addr{font-size:12.5px;line-height:20px;display:flex;gap:18px}
.newsletter-note{left:848px;top:4562px;font-size:11.5px}
.email-field{left:848px;top:4603px;width:236px;height:38px;background:var(--white);color:#555;font-size:12px;padding:12px 14px}
.sub-btn{left:848px;top:4655px;width:236px;height:36px;background:var(--blue);color:var(--white);font-size:12px;font-weight:700;text-align:center;line-height:36px}
.f-rule{left:113px;top:4770px;width:974px;height:1px;background:rgba(255,255,255,.12)}
.socials{left:113px;top:4795px;display:flex;gap:8px}
.socials i{width:30px;height:30px;border:2px solid var(--footer-text);border-radius:50%;display:block}
.copy{right:113px;top:4802px;font-size:12.5px}
</style>
</head>
<body>

<header class="abs hero">
  <div class="hero-photo" role="img" aria-label="Photo of a doctor at a desk with a laptop consulting a patient"></div>
  <div class="hero-shade"></div>
</header>
<div class="abs logo">Medvira</div>
<nav class="abs nav"><a>About Us</a><a>Our services</a><a>Health tips</a><a>Help</a><a>Contact Us</a>
  <svg width="14" height="14" viewBox="0 0 14 14"><circle cx="6" cy="6" r="4.5" fill="none" stroke="#fff" stroke-width="2"/><path d="M9.5 9.5L13 13" stroke="#fff" stroke-width="2"/></svg></nav>
<a class="abs member-btn"><svg width="12" height="12" viewBox="0 0 12 12"><circle cx="6" cy="3.5" r="3" fill="#fff"/><path d="M0 12c0-4 12-4 12 0z" fill="#fff"/></svg>MEMBER LOGIN</a>
<div class="abs lang"><i></i>ENG ▾</div>
<h1 class="abs center hero-title">FIND A DOCTOR</h1>
<p class="abs center hero-lead">Lorem ipsum dolor sit amet, consectetur adipiscin sed do eiusmod tempor<br>incididunt ut labore et dolore magna aliqed minim veniam</p>
<div class="abs search"><span>Find doctor</span>
  <div class="search-btn"><svg width="14" height="14" viewBox="0 0 14 14"><circle cx="6" cy="6" r="4.5" fill="none" stroke="#fff" stroke-width="2"/><path d="M9.5 9.5L13 13" stroke="#fff" stroke-width="2"/></svg>SEARCH</div></div>
<div class="abs dots"><i></i><i></i><i class="on"></i><i></i><i></i></div>

<!-- services -->
<div class="abs center ghost" style="top:885px;left:30px">OUR SERVICES</div>
<h2 class="abs center sec-title" style="top:912px">OUR SERVICES</h2>
<p class="abs center sec-sub" style="top:993px">Lorem ipsum dolor sit amet consectetur adipiscing elit sed do eiusmod</p>
<div class="abs rule" style="top:1043px"></div>

<div class="abs service" style="left:86px;top:1141px">
  <svg width="154" height="150" viewBox="0 0 154 150"><polygon points="40,3 114,3 151,75 114,147 40,147 3,75" fill="none" stroke="#1f7fc0" stroke-width="2.5"/>
  <g fill="#1f7fc0"><circle cx="77" cy="63" r="9"/><circle cx="58" cy="67" r="7"/><circle cx="96" cy="67" r="7"/><path d="M62 96c0-20 30-20 30 0z"/><path d="M45 94c0-16 22-16 22-4v4z"/><path d="M87 94v-4c0-12 22-12 22 4z"/></g></svg>
  <h3>LOREM IPSUMD</h3>
  <p>Lorem ipsum dolor sit amet, consectetur<br>adipiscing elit. Donec lorem maximus male<br>suada lorem maximus mauris.</p>
</div>
<div class="abs service" style="left:448px;top:1141px">
  <svg width="154" height="150" viewBox="0 0 154 150"><polygon points="40,3 114,3 151,75 114,147 40,147 3,75" fill="none" stroke="#1f7fc0" stroke-width="2.5"/>
  <g fill="#1f7fc0"><rect x="48" y="58" width="44" height="34" rx="3"/><path d="M92 66h12l10 12v14H92z"/><circle cx="60" cy="94" r="7"/><circle cx="100" cy="94" r="7"/></g>
  <path d="M70 66v18M61 75h18" stroke="#fff" stroke-width="5"/></svg>
  <h3>ITATION ULLAMCO</h3>
  <p>Lorem ipsum dolor sit amet, consectetur<br>adipiscing elit. Donec lorem maximus male<br>suada lorem maximus mauris.</p>
</div>
<div class="abs service" style="left:814px;top:1141px">
  <svg width="154" height="150" viewBox="0 0 154 150"><polygon points="40,3 114,3 151,75 114,147 40,147 3,75" fill="none" stroke="#1f7fc0" stroke-width="2.5"/>
  <g fill="none" stroke="#1f7fc0" stroke-width="5" stroke-linecap="round"><circle cx="70" cy="86" r="15"/><path d="M66 60v22h20l8 16"/></g><circle cx="66" cy="50" r="6" fill="#1f7fc0"/></svg>
  <h3>MAGNA ALIQ</h3>
  <p>Lorem ipsum dolor sit amet, consectetur<br>adipiscing elit. Donec lorem maximus male<br>suada lorem maximus mauris.</p>
</div>
<a class="abs pill" style="left:479px;top:1527px;width:240px">VIEW ALL SERVICES <svg width="14" height="14" viewBox="0 0 14 14"><circle cx="7" cy="7" r="7" fill="#fff"/><path d="M5.5 4l3 3-3 3" stroke="#1f7fc0" stroke-width="2" fill="none"/></svg></a>

<!-- about -->
<section class="abs about"></section>
<div class="abs ghost about-ghost">ARE</div>
<h2 class="abs about-title">WHO WE ARE</h2>
<p class="abs about-text">Lorem ipsum dolor sit amet, consectetur adipiscing elit, sed do eiusmod tempor incididunt ut labore et dolore magna aliqua. Ut enim ad minim veniam, quis nostrud exercitation ullamco laboris nisi ut aliquip ex ea commodo consequat. Duis aute irure dolor in reprehenderit in voluptate velit esse cillum dolore</p>
<a class="abs read-btn">READ MORE <svg width="14" height="14" viewBox="0 0 14 14"><circle cx="7" cy="7" r="7" fill="#fff"/><path d="M5.5 4l3 3-3 3" stroke="#1f7fc0" stroke-width="2" fill="none"/></svg></a>
<div class="abs photo about-photo" role="img" aria-label="Photo of a doctor in a suit and a nurse holding a clipboard in a hospital corridor"></div>

<!-- health tips -->
<section class="abs tips"></section>
<div class="abs center ghost light" style="top:2430px">HEALTH TIPS</div>
<h2 class="abs center sec-title" style="top:2485px;color:#fff">HEALTH TIPS</h2>
<p class="abs center sec-sub" style="top:2565px;color:#fff">Lorem ipsum dolor sit amet consectetur adipiscing elit.</p>
<div class="abs rule" style="top:2605px;background:#fff"></div>
<div class="abs tips-box"></div>
<div class="abs photo tips-photo" role="img" aria-label="Photo of a doctor shaking hands with a patient in a clinic"></div>
<ul class="abs tips-list">
  <li><svg width="14" height="14" viewBox="0 0 14 14"><circle cx="7" cy="7" r="7" fill="#fff"/><path d="M5.5 4l3 3-3 3" stroke="#1f7fc0" stroke-width="2" fill="none"/></svg>Sed ut perspiciatis unde omnis iste natus</li>
  <li><svg width="14" height="14" viewBox="0 0 14 14"><circle cx="7" cy="7" r="7" fill="#fff"/><path d="M5.5 4l3 3-3 3" stroke="#1f7fc0" stroke-width="2" fill="none"/></svg>Error sit voluptatem accusantium dolore</li>
  <li><svg width="14" height="14" viewBox="0 0 14 14"><circle cx="7" cy="7" r="7" fill="#fff"/><path d="M5.5 4l3 3-3 3" stroke="#1f7fc0" stroke-width="2" fill="none"/></svg>Mut laudantium totam rem aperiam</li>
  <li><svg width="14" height="14" viewBox="0 0 14 14"><circle cx="7" cy="7" r="7" fill="#fff"/><path d="M5.5 4l3 3-3 3" stroke="#1f7fc0" stroke-width="2" fill="none"/></svg>Excepteur sint occaecat cupidata</li>
  <li><svg width="14" height="14" viewBox="0 0 14 14"><circle cx="7" cy="7" r="7" fill="#fff"/><path d="M5.5 4l3 3-3 3" stroke="#1f7fc0" stroke-width="2" fill="none"/></svg>Duis aute irure dolor in reprehenderit in voluptate</li>
  <li><svg width="14" height="14" viewBox="0 0 14 14"><circle cx="7" cy="7" r="7" fill="#fff"/><path d="M5.5 4l3 3-3 3" stroke="#1f7fc0" stroke-width="2" fill="none"/></svg>velit esse cillum dolore eu fugiat nulla pariatur.</li>
</ul>
<a class="abs outline-btn">READ MORE <svg width="14" height="14" viewBox="0 0 14 14"><circle cx="7" cy="7" r="7" fill="#fff"/><path d="M5.5 4l3 3-3 3" stroke="#1f7fc0" stroke-width="2" fill="none"/></svg></a>

<!-- help -->
<div class="abs center ghost" style="top:3335px;left:-50px">HELP</div>
<h2 class="abs center sec-title" style="top:3377px">HELP</h2>
<div class="abs rule" style="top:3452px"></div>
<p class="abs center sec-sub" style="top:3497px">Lorem ipsum dolor sit amet, consectetur adipiscin nisi ut aliquip ex ea commodo consequat.</p>
<div class="abs photo video" role="img" aria-label="Video still of a doctor and medical staff in a hospital"></div>
<svg class="abs" style="left:563px;top:3737px" width="74" height="74" viewBox="0 0 74 74"><circle cx="37" cy="37" r="34" fill="rgba(0,0,0,.25)" stroke="#fff" stroke-width="4"/><path d="M29 23l22 14-22 14z" fill="#fff"/></svg>
<ul class="abs help-list" style="left:300px">
  <li><svg width="16" height="16" viewBox="0 0 14 14"><circle cx="7" cy="7" r="7" fill="#1f7fc0"/><path d="M5.5 4l3 3-3 3" stroke="#fff" stroke-width="2" fill="none"/></svg>Lorem ipsum doit aconseurnim</li>
  <li><svg width="16" height="16" viewBox="0 0 14 14"><circle cx="7" cy="7" r="7" fill="#1f7fc0"/><path d="M5.5 4l3 3-3 3" stroke="#fff" stroke-width="2" fill="none"/></svg>Nisi ut aliquicommodo</li>
  <li><svg width="16" height="16" viewBox="0 0 14 14"><circle cx="7" cy="7" r="7" fill="#1f7fc0"/><path d="M5.5 4l3 3-3 3" stroke="#fff" stroke-width="2" fill="none"/></svg>Eusmod teincididunt</li>
</ul>
<ul class="abs help-list" style="left:628px">
  <li><svg width="16" height="16" viewBox="0 0 14 14"><circle cx="7" cy="7" r="7" fill="#1f7fc0"/><path d="M5.5 4l3 3-3 3" stroke="#fff" stroke-width="2" fill="none"/></svg>Ullamco laboris nisimodoc</li>
  <li><svg width="16" height="16" viewBox="0 0 14 14"><circle cx="7" cy="7" r="7" fill="#1f7fc0"/><path d="M5.5 4l3 3-3 3" stroke="#fff" stroke-width="2" fill="none"/></svg>Duis aute irure dolor</li>
  <li><svg width="16" height="16" viewBox="0 0 14 14"><circle cx="7" cy="7" r="7" fill="#1f7fc0"/><path d="M5.5 4l3 3-3 3" stroke="#fff" stroke-width="2" fill="none"/></svg>Consequuntur magni dolores</li>
</ul>
<a class="abs pill" style="left:476px;top:4244px;width:249px;height:50px">VIEW MORE TIPS <svg width="14" height="14" viewBox="0 0 14 14"><circle cx="7" cy="7" r="7" fill="#fff"/><path d="M5.5 4l3 3-3 3" stroke="#1f7fc0" stroke-width="2" fill="none"/></svg></a>

<!-- footer -->
<footer class="abs footer"></footer>
<h4 class="abs f-head" style="left:113px">ADDRESS</h4>
<h4 class="abs f-head" style="left:404px">QUICK LINKS</h4>
<h4 class="abs f-head" style="left:615px">GLOSSARY</h4>
<h4 class="abs f-head" style="left:848px">SUBSCRIBE TO NEWSLETTER</h4>
<div class="abs addr footer-text" style="left:113px;top:4550px"><svg width="14" height="18" viewBox="0 0 14 18"><path d="M7 1a6 6 0 0 1 6 6c0 4-6 10-6 10S1 11 1 7a6 6 0 0 1 6-6z" fill="none" stroke="#dfe4e8" stroke-width="1.5"/><circle cx="7" cy="7" r="2" fill="#dfe4e8"/></svg><span>35 Sed ut perspiciatis omni<br>iste natus error.</span></div>
<div class="abs addr footer-text" style="left:113px;top:4610px"><svg width="16" height="16" viewBox="0 0 16 16"><path d="M3 1l3 3-2 2c1 3 3 5 6 6l2-2 3 3-2 2C7 15 1 9 1 3z" fill="none" stroke="#dfe4e8" stroke-width="1.5"/></svg><span>Phone: 1 800 555 0134</span></div>
<div class="abs addr footer-text" style="left:113px;top:4655px"><svg width="16" height="12" viewBox="0 0 16 12"><rect x="1" y="1" width="14" height="10" fill="none" stroke="#dfe4e8" stroke-width="1.5"/><path d="M1 1l7 6 7-6" fill="none" stroke="#dfe4e8" stroke-width="1.5"/></svg><span>info@clinicname.example</span></div>
<ul class="abs f-list footer-text" style="left:404px;top:4544px">
  <li><svg width="8" height="10" viewBox="0 0 8 10"><path d="M1 1l6 4-6 4z" fill="#dfe4e8"/></svg>Privacy Policy</li>
  <li><svg width="8" height="10" viewBox="0 0 8 10"><path d="M1 1l6 4-6 4z" fill="#dfe4e8"/></svg>Terms and use</li>
  <li><svg width="8" height="10" viewBox="0 0 8 10"><path d="M1 1l6 4-6 4z" fill="#dfe4e8"/></svg>Sitemap</li>
  <li><svg width="8" height="10" viewBox="0 0 8 10"><path d="M1 1l6 4-6 4z" fill="#dfe4e8"/></svg>Information</li>
</ul>
<ul class="abs f-list footer-text" style="left:615px;top:4544px">
  <li><svg width="8" height="10" viewBox="0 0 8 10"><path d="M1 1l6 4-6 4z" fill="#dfe4e8"/></svg>Sed ut perspiciatis</li>
  <li><svg width="8" height="10" viewBox="0 0 8 10"><path d="M1 1l6 4-6 4z" fill="#dfe4e8"/></svg>Unde omnis iste natus</li>
  <li><svg width="8" height="10" viewBox="0 0 8 10"><path d="M1 1l6 4-6 4z" fill="#dfe4e8"/></svg>Error sit voluptatem</li>
  <li><svg width="8" height="10" viewBox="0 0 8 10"><path d="M1 1l6 4-6 4z" fill="#dfe4e8"/></svg>Aacusantium</li>
</ul>
<p class="abs newsletter-note footer-text">Subscribe and we'll automatically send you</p>
<div class="abs email-field">Enter Email</div>
<div class="abs sub-btn">SUBSCRIBE</div>
<div class="abs f-rule"></div>
<div class="abs socials"><i></i><i></i><i></i><i></i></div>
<p class="abs copy footer-text">Copyright © 2019 Clinicname. All rights reserved.</p>

</body>
</html>
```